" Prospectamos pequenas e médias empresas que necessitam de uma presença na internet para melhorar seus resultados, e oferecemos as melhores soluções para cada negócio. Criamos desde landing pages básicas, até grandes sites com gerenciamento de conteúdo. Otimização para mecanismos de busca, gestão de campanhas de links patrocinados, gestão de blogs e redes sociais, sistemas personalizados, infra estrutura de TI. "

```html
<!DOCTYPE html>
<html lang="pt-BR">
<head>
<meta charset="UTF-8">
<title>Vertexa Digital – Flyer</title>
<link rel="stylesheet" href="https://fonts.googleapis.com/css2?family=Montserrat:wght@600;700;800&family=Open+Sans:wght@400;600&display=swap">
<style>
  :root{
    --page-bg:#e9e7e4;
    --paper:#ffffff;
    --navy:#1e3a84;
    --navy-deep:#172e6b;
    --navy-light:#2a4b9e;
    --orange:#e8622c;
    --clay:#b4572f;
    --clay-dark:#7e3a1f;
    --clay-light:#d08a5e;
    --white:#ffffff;
    --soft:#cfd8ef;
  }
  *{box-sizing:border-box;margin:0;padding:0}
  html,body{width:1200px;height:1200px;overflow:hidden}
  body{background:var(--page-bg);font-family:"Open Sans",Arial,sans-serif;position:relative}
  .flyer{position:absolute;left:204px;top:40px;width:792px;height:1120px;background:var(--paper);overflow:hidden;box-shadow:0 10px 30px rgba(0,0,0,.18)}
  .hero-photo{position:absolute;left:0;top:0;width:100%;height:660px;
    background:radial-gradient(ellipse at 55% 60%,var(--clay-light) 0%,var(--clay) 45%,var(--clay-dark) 100%)}
  .top-band{position:absolute;left:0;top:0;width:100%;height:260px;background:var(--paper);
    clip-path:polygon(0 0,100% 0,100% 42%,0 100%)}
  .brand{position:absolute;left:44px;top:62px;display:flex;align-items:center;gap:14px}
  .brand-dot{width:58px;height:58px;border-radius:50%;border:8px solid var(--orange)}
  .brand-name{font-family:"Montserrat",Arial,sans-serif;font-weight:700;font-size:46px;color:var(--navy);letter-spacing:.5px}
  .globe{position:absolute;left:598px;top:470px;width:96px;height:96px}
  .panel{position:absolute;left:0;top:0;width:100%;height:100%;background:var(--navy);
    clip-path:polygon(0 590px,100% 520px,100% 100%,0 100%)}
  .headline{position:absolute;left:52px;top:628px;font-family:"Montserrat",Arial,sans-serif;font-weight:800;
    font-size:43px;line-height:1.08;color:var(--white);text-transform:uppercase}
  .headline .accent{color:var(--orange)}
  .intro{position:absolute;left:52px;top:770px;width:690px;font-size:17px;line-height:1.55;color:var(--white)}
  .contact-bar{position:absolute;left:0;bottom:0;width:100%;height:130px;background:var(--navy-deep);
    display:grid;grid-template-columns:1.6fr 1fr;gap:14px 24px;padding:32px 52px;align-content:center}
  .contact-item{display:flex;align-items:center;gap:10px;font-size:14px;color:var(--soft)}
  .contact-item svg{flex:none;width:18px;height:18px}
  .phone-line{position:absolute;right:52px;top:900px;display:flex;gap:10px;align-items:center;font-size:15px;color:var(--white)}
  .dot-icon{width:14px;height:14px;border-radius:50%;background:var(--soft)}
</style>
</head>
<body>
  <main class="flyer">
    <div class="hero-photo" role="img" aria-label="Photo of a tortoise and a hare at the start line of a clay running track"></div>
    <div class="top-band"></div>
    <div class="brand">
      <span class="brand-dot"></span>
      <span class="brand-name">vertexa digital</span>
    </div>

    <div class="panel"></div>

    <svg class="globe" viewBox="0 0 100 100" aria-hidden="true">
      <circle cx="50" cy="50" r="40" fill="none" stroke="var(--orange)" stroke-width="5"/>
      <ellipse cx="50" cy="50" rx="17" ry="40" fill="none" stroke="var(--orange)" stroke-width="4"/>
      <line x1="10" y1="50" x2="90" y2="50" stroke="var(--orange)" stroke-width="4"/>
      <path d="M17 30 H83 M17 70 H83" stroke="var(--orange)" stroke-width="4" fill="none"/>
    </svg>

    <h1 class="headline">Seus negócios estão<br><span class="accent">ou não estão</span> na internet?</h1>

    <p class="intro">Criamos de landing pages básicas, a grandes sites com gerenciamento de conteúdo. Otimização para mecanismos de busca, gestão de campanhas de links patrocinados, gestão de blogs e redes sociais, sistemas personalizados, infra estrutura de TI.</p>

    <div class="phone-line"><span class="dot-icon"></span>(00) 4321-8765</div>

    <footer class="contact-bar">
      <div class="contact-item">
        <svg viewBox="0 0 24 24"><path d="M12 2a7 7 0 0 0-7 7c0 5 7 13 7 13s7-8 7-13a7 7 0 0 0-7-7zm0 9.5A2.5 2.5 0 1 1 12 6.5a2.5 2.5 0 0 1 0 5z" fill="var(--soft)"/></svg>
        Av. Nome da Avenida, 222 - Nome do Bairro - Cidade - UF
      </div>
      <div class="contact-item">
        <svg viewBox="0 0 24 24"><circle cx="12" cy="12" r="9" fill="none" stroke="var(--soft)" stroke-width="2"/><path d="M3 12h18M12 3c3 3 3 15 0 18M12 3c-3 3-3 15 0 18" fill="none" stroke="var(--soft)" stroke-width="1.6"/></svg>
        www.vertexa.com.br
      </div>
      <div class="contact-item">
        <svg viewBox="0 0 24 24"><rect x="3" y="5" width="18" height="14" rx="2" fill="none" stroke="var(--soft)" stroke-width="2"/><path d="M3 7l9 6 9-6" fill="none" stroke="var(--soft)" stroke-width="2"/></svg>
        contato@vertexa.com.br
      </div>
      <div class="contact-item">
        <svg viewBox="0 0 24 24"><circle cx="12" cy="12" r="9" fill="var(--soft)"/></svg>
        /vertexadigital
      </div>
    </footer>
  </main>
</body>
</html>
```